A professional I.T consulting company requires a web design

Our company needs a fresh web design to help us drive our business forward. We are an Information Technology company who specialises in solutions based I.T delivery and consultations and who prides ourselves on our professional approach to business.

We would like a web site design from a designer who may be able to help us upload the site to WordPress and who may be interested in completing the "coding" section of the site (minimal coding). Although this is not essential to this project and won't factor into the decision making process.

A very thorough brief has been put together for this design project so very limited work is required in regards to content (the brief sets out all the content text - copy write material).

Please see the attached project documents for a copy of the brief

Target Market(s)

Please refer to the attached brief

Industry/Entity Type

Business

Requirements
Must have
• Please refer to the attached brief
Nice to have
Should not have

```html
<!DOCTYPE html>
<html lang="en">
<head>
<meta charset="utf-8">
<title>Korvant — IT Solutions</title>
<link rel="stylesheet" href="https://fonts.googleapis.com/css2?family=Questrial&family=Roboto:wght@400;500&display=swap">
<style>
:root{
  --blue:#1f78b8;
  --blue-dark:#0f4f82;
  --blue-deep:#0b3a60;
  --blue-light:#49a6de;
  --sky:#2aa3e0;
  --paper:#f1f2f4;
  --panel:#ececee;
  --text:#6b6b6b;
  --footer:#4a4a4a;
  --footer-line:#5e5e5e;
  --white:#ffffff;
}
*{box-sizing:border-box;margin:0;padding:0}
html,body{width:816px;height:1200px;overflow:hidden}
body{position:relative;background:var(--paper);font-family:"Roboto",sans-serif;color:var(--text)}
.abs{position:absolute}

/* header */
.brand{left:38px;top:16px;display:flex;align-items:center;gap:8px}
.brand-dot{width:52px;height:52px;border-radius:50%;background:var(--sky)}
.brand-name{font-family:"Questrial",sans-serif;font-size:30px;color:var(--sky);letter-spacing:1px;line-height:1}
.brand-tag{font-family:"Questrial",sans-serif;font-size:8px;letter-spacing:2px;color:#8a8a8a;margin-top:2px}
.social{right:52px;top:21px;display:flex;gap:5px}
.social span{width:21px;height:21px;border-radius:50%;background:var(--blue)}
.social span:last-child{background:#e9902a}
.callout{right:50px;top:52px;display:flex;align-items:center;gap:6px}
.callout .icon{width:26px;height:26px;border-radius:4px;background:var(--sky);display:flex;align-items:center;justify-content:center}
.callout small{display:block;font-family:"Questrial",sans-serif;font-size:9px;letter-spacing:1px;color:#888}
.callout strong{display:block;font-family:"Questrial",sans-serif;font-weight:400;font-size:15px;letter-spacing:1px;color:var(--blue)}

/* nav */
.nav{left:0;top:92px;width:816px;height:32px;background:linear-gradient(#3692d0,#1a6aa8)}
.nav ul{list-style:none}
.nav li{position:absolute;top:0;font-family:"Questrial",sans-serif;font-size:9.5px;letter-spacing:.8px;color:var(--white);line-height:32px;white-space:nowrap}
.nav li.current{background:var(--blue-dark);padding:0 6px}
.search{left:625px;top:96px;width:149px;height:24px;display:flex}
.search input{width:109px;height:24px;border:0;padding-left:9px;font-family:"Questrial",sans-serif;font-size:10px;color:#aaa;background:#fff}
.search button{width:40px;height:24px;border:0;background:var(--blue-dark);display:flex;align-items:center;justify-content:center}

/* hero */
.hero{left:32px;top:143px;width:752px;height:330px;border-radius:6px;background:#d8d9db;padding:5px}
.hero-photo{left:5px;top:5px;width:440px;height:320px;background:linear-gradient(120deg,#2c2c2e,#6b7178 55%,#9aa3ab);clip-path:polygon(0 0,100% 0,70% 100%,0 100%);border-radius:4px 0 0 4px}
.hero-panel{left:5px;top:5px;width:742px;height:320px;border-radius:4px;background:linear-gradient(135deg,#2c6e9e,#1d5784 50%,#0e3c62);clip-path:polygon(60% 0,100% 0,100% 100%,41% 100%)}
.hero-stripe{left:5px;top:5px;width:742px;height:320px;background:var(--sky);clip-path:polygon(57% 0,60% 0,41% 100%,38% 100%)}
.welcome{left:478px;top:43px;width:250px;text-align:center;color:var(--white)}
.welcome small{display:block;font-family:"Questrial",sans-serif;font-size:10px;letter-spacing:1px;margin-left:-40px}
.welcome .hero-name{display:flex;align-items:center;justify-content:center;gap:6px;font-family:"Questrial",sans-serif;font-size:28px;color:#d7e9f6;margin-top:2px}
.welcome .hero-name i{width:34px;height:34px;border-radius:50%;background:#d7e9f6;display:block}
.welcome .tag{font-family:"Questrial",sans-serif;font-size:7px;letter-spacing:2px;color:#6c94b5;margin-top:2px}
.hero-copy{left:410px;top:112px;width:292px;font-family:"Questrial",sans-serif;font-size:11px;line-height:19.6px;letter-spacing:1px;color:var(--white);text-align:justify;text-align-last:center}
.dots{left:665px;top:297px;display:flex;gap:6px}
.dots span{width:10px;height:10px;border-radius:50%;background:#dfe6ec;border:2px solid #2a5f88}
.dots span:first-child{background:var(--sky)}

/* features */
.features{left:32px;top:484px;width:752px;height:284px;border-radius:4px;background:linear-gradient(#f7f7f8,var(--panel));border:1px solid #e0e0e2}
.card{top:22px;width:216px}
.card-head{height:24px;background:linear-gradient(var(--blue),var(--blue-dark));font-family:"Questrial",sans-serif;font-size:11px;letter-spacing:1px;color:var(--white);line-height:24px;padding-left:9px;position:relative}
.card-head .badge{position:absolute;right:8px;top:-6px;width:36px;height:36px;border-radius:50%;background:var(--blue-dark);border:3px solid var(--white);display:flex;align-items:center;justify-content:center}
.card-img{height:143px}
.card p{font-size:9.5px;line-height:12px;letter-spacing:.8px;color:#8a8a8a;text-align:justify;margin-top:11px;height:36px;overflow:hidden;padding:0 1px}
.card .rule{border-top:1px solid #d4d4d4;margin-top:13px}
.more{display:block;width:58px;margin:-10px auto 0;height:19px;border-radius:3px;background:var(--blue-dark);font-family:"Questrial",sans-serif;font-size:9.5px;letter-spacing:1px;color:var(--white);text-align:center;line-height:19px}

/* partners */
.partners{left:32px;top:825px;width:752px;height:40px;display:flex;align-items:center;justify-content:space-between}
.partners .arrow{width:16px}
.partner{height:34px;border-radius:17px;background:#d1d5da}

/* footer */
.footer{left:0;top:917px;width:816px;height:259px;background:linear-gradient(var(--footer),#3d3d3d)}
.col-title{font-family:"Questrial",sans-serif;font-size:12.5px;letter-spacing:1px;color:var(--white);padding-bottom:5px;border-bottom:1px solid var(--footer-line)}
.testimonial{display:flex;gap:14px;padding:10px 0 10px 2px;border-bottom:1px solid var(--footer-line)}
.portrait{width:66px;height:66px;flex:none;border:4px solid #333;background:linear-gradient(#c9cdd2,#8b9098)}
.testimonial p{font-size:8px;line-height:12px;letter-spacing:.5px;color:#e4e4e4}
.testimonial cite{display:block;font-style:normal;color:var(--sky);text-transform:uppercase}
.view-all{font-family:"Questrial",sans-serif;font-size:9.5px;line-height:11px;letter-spacing:1px;color:#e4e4e4;margin:8px 0 0 5px}
.links{list-style:none;margin-top:8px;height:181px;border-bottom:1px solid var(--footer-line)}
.links li{font-family:"Questrial",sans-serif;font-size:11.5px;letter-spacing:1px;color:#eee;line-height:23.2px;padding-left:14px;position:relative}
.links li::before{content:"›";position:absolute;left:0;color:#ccc}
.loc{display:flex;gap:10px;font-family:"Questrial",sans-serif;font-size:9.5px;letter-spacing:.8px;color:#eee;line-height:13px;margin-top:9px;white-space:nowrap}
.loc svg{flex:none;margin-top:1px}
.foot-social{display:flex;gap:6px;margin:22px 0 0 6px}
.foot-social span{width:22px;height:22px;border-radius:50%;background:#d6d6d6}
.loc-rule{position:absolute;left:0;top:188px;width:156px;border-top:1px solid var(--footer-line)}
.bottom{left:0;top:1176px;width:816px;height:24px;background:var(--blue);font-family:"Questrial",sans-serif;font-size:8.5px;letter-spacing:1px;color:var(--white);line-height:24px}
</style>
</head>
<body>

<header>
  <div class="brand abs">
    <div class="brand-dot"></div>
    <div>
      <div class="brand-name">KORVANT</div>
      <div class="brand-tag">NO EXCUSES. JUST RESULTS</div>
    </div>
  </div>
  <div class="social abs" aria-label="Social links"><span></span><span></span><span></span><span></span></div>
  <div class="callout abs">
    <div class="icon"><svg width="14" height="14" viewBox="0 0 24 24"><path fill="#fff" d="M6.6 10.8a15 15 0 0 0 6.6 6.6l2.2-2.2c.3-.3.7-.4 1-.2 1.1.4 2.3.6 3.6.6.6 0 1 .4 1 1V20c0 .6-.4 1-1 1A17 17 0 0 1 3 4c0-.6.4-1 1-1h3.5c.6 0 1 .4 1 1 0 1.3.2 2.5.6 3.6.1.3 0 .7-.2 1z"/></svg></div>
    <div><small>CALL US TOLL FREE</small><strong>1300 555 019</strong></div>
  </div>
</header>

<nav class="nav abs">
  <ul>
    <li class="current" style="left:38px">HOME</li>
    <li style="left:99px">ABOUT US</li>
    <li style="left:172px">WHY KORVANT?</li>
    <li style="left:268px">SERVICES</li>
    <li style="left:342px">SOLUTIONS</li>
    <li style="left:426px">TECHNOLOGIES</li>
    <li style="left:533px">CONTACT</li>
  </ul>
</nav>
<form class="search abs">
  <input type="text" placeholder="Search">
  <button type="button" aria-label="Search"><svg width="15" height="15" viewBox="0 0 24 24"><circle cx="14" cy="10" r="6" fill="none" stroke="#fff" stroke-width="3"/><path d="M9.5 14.5 3 21" stroke="#fff" stroke-width="4" stroke-linecap="round"/></svg></button>
</form>

<section class="hero abs">
  <div class="hero-photo abs" role="img" aria-label="Businessman in a suit holding a tablet and a glowing network globe"></div>
  <div class="hero-panel abs"></div>
  <div class="hero-stripe abs"></div>
  <div class="welcome abs">
    <small>WELCOME TO</small>
    <div class="hero-name"><i></i>KORVANT</div>
    <div class="tag">NO EXCUSES. JUST RESULTS</div>
  </div>
  <p class="hero-copy abs">KORVANT provides quality Information Technology support and solutions services for businesses throughout the Latrobe Valley and the greater Metropolitan areas. We pride ourselves on our professional approach to our service delivery and in our no-nonsense approach to meeting our client’s unique business I.T needs.</p>
  <div class="dots abs"><span></span><span></span><span></span></div>
</section>

<section class="features abs">
  <article class="card abs" style="left:27px">
    <div class="card-head">OUR SERVICES<span class="badge"><svg width="16" height="16" viewBox="0 0 24 24"><path d="M4 4l16 16M20 4 4 20" stroke="#fff" stroke-width="3" stroke-linecap="round"/></svg></span></div>
    <div class="card-img" role="img" aria-label="Glowing globe surrounded by rings of computer screens" style="background:radial-gradient(circle at 50% 50%,#7fd3ff,#1a5fb4 35%,#08214a 80%)"></div>
    <p>When it comes to your business’s I.T service needs, KORVANT provides you with expertly delivered, unique I.T services,</p>
    <div class="rule"></div><span class="more">read more</span>
  </article>
  <article class="card abs" style="left:268px">
    <div class="card-head">OUR SOLUTIONS<span class="badge"><svg width="16" height="16" viewBox="0 0 24 24"><ellipse cx="11" cy="6" rx="7" ry="3" fill="#fff"/><path d="M4 9v8c0 1.7 3 3 7 3" fill="none" stroke="#fff" stroke-width="2.5"/><path d="M18 13v8M14 17h8" stroke="#fff" stroke-width="2.5"/></svg></span></div>
    <div class="card-img" role="img" aria-label="Hand holding a glowing laptop with floating digital icons" style="background:radial-gradient(circle at 55% 55%,#d7ecf8,#4a86b0 30%,#0a1a2c 75%)"></div>
    <p>KORVANT began as solutions specialist and continues to lead the industry with our skills and experience in market leading technolo-</p>
    <div class="rule"></div><span class="more">read more</span>
  </article>
  <article class="card abs" style="left:509px">
    <div class="card-head">OUR TECHNOLOGIES<span class="badge"><svg width="16" height="16" viewBox="0 0 24 24"><path d="M20 4c-6 0-10 4-12 9l3 3c5-2 9-6 9-12zM8 13l-4 1 2 2M11 16l-1 4 2-2" fill="#fff"/></svg></span></div>
    <div class="card-img" role="img" aria-label="Close-up of a blue circuit board" style="background:linear-gradient(135deg,#6cb3e6,#1d5e9c 50%,#a7c65a 85%)"></div>
    <p>KORVANT engineers are highly skilled with experience in a diverse range of technologies. Our Engineers are certified in Veloria,</p>
    <div class="rule"></div><span class="more">read more</span>
  </article>
</section>

<section class="partners abs" aria-label="Technology partners">
  <svg class="arrow" width="16" height="22" viewBox="0 0 16 22"><path d="M12 2 3 11l9 9" fill="none" stroke="#9a9a9a" stroke-width="1.5"/></svg>
  <div class="partner" style="width:138px"></div>
  <div class="partner" style="width:126px"></div>
  <div class="partner" style="width:78px"></div>
  <div class="partner" style="width:46px;border-radius:50%;height:46px"></div>
  <div class="partner" style="width:90px"></div>
  <div class="partner" style="width:90px"></div>
  <svg class="arrow" width="16" height="22" viewBox="0 0 16 22"><path d="M4 2l9 9-9 9" fill="none" stroke="#9a9a9a" stroke-width="1.5"/></svg>
</section>

<footer class="footer abs">
  <div class="abs" style="left:68px;top:26px;width:272px">
    <h3 class="col-title">TESTIMONIALS</h3>
    <div class="testimonial">
      <div class="portrait" role="img" aria-label="Portrait photo of a client"></div>
      <p>The staff at KORVANT are the most enthusiastic and personable people I have met and have an extensive IT knowledge and thirst for greater knowledge<cite>- Daniel Ashcombe,</cite></p>
    </div>
    <div class="testimonial">
      <div class="portrait" role="img" aria-label="Portrait photo of a client"></div>
      <p>The staff at KORVANT are the most enthusiastic and personable people I have met and has an extensive IT knowledge and thirst for greater knowledge.<cite>- Liam Foreshaw,</cite></p>
    </div>
    <div class="view-all">VIEW ALL</div>
  </div>
  <div class="abs" style="left:386px;top:26px;width:156px">
    <h3 class="col-title">QUICKLINKS</h3>
    <ul class="links"><li>Home</li><li>About us</li><li>Why KORVANT?</li><li>Services</li><li>Solutions</li><li>Technologies</li></ul>
  </div>
  <div class="abs" style="left:602px;top:26px;width:156px;height:200px">
    <h3 class="col-title">LOCATION</h3>
    <div class="loc"><svg width="12" height="12" viewBox="0 0 24 24"><path d="M12 2 1 12h3v10h6v-6h4v6h6V12h3z" fill="#ddd"/></svg><span>218 HARBOUR LANE,<br>RIVERTON, VC<br>3840</span></div>
    <div class="loc"><svg width="12" height="12" viewBox="0 0 24 24"><path d="M6.6 10.8a15 15 0 0 0 6.6 6.6l2.2-2.2c.3-.3.7-.4 1-.2 1.1.4 2.3.6 3.6.6.6 0 1 .4 1 1V20c0 .6-.4 1-1 1A17 17 0 0 1 3 4c0-.6.4-1 1-1h3.5c.6 0 1 .4 1 1 0 1.3.2 2.5.6 3.6.1.3 0 .7-.2 1z" fill="#ddd"/></svg><span>1300 555 019</span></div>
    <div class="loc"><svg width="14" height="12" viewBox="0 0 24 18"><rect x="1" y="1" width="22" height="16" fill="#ddd"/><path d="M1 1l11 9 11-9" fill="none" stroke="#4a4a4a" stroke-width="2"/></svg><span>hello@korvant.example</span></div>
    <div class="foot-social" aria-label="Social links"><span></span><span></span><span></span><span></span></div>
    <div class="loc-rule"></div>
  </div>
</footer>

<div class="bottom abs">
  <span class="abs" style="left:65px">Copyright 2014 · All rights reserved</span>
  <span class="abs" style="right:54px">Sitemap &nbsp; | &nbsp; FAQ &nbsp; | &nbsp; Privacy Policy</span>
</div>

</body>
</html>
```